Infografiken für Rechtsfirma
Zielgruppe
Wir sind eine Rechtsfirma, welche sich mit dem europäischen Recht beschäftigt. Wir bieten Insolvenzen in unterschiedlichen Ländern an. Weiter beraten wir hinsichtlich des Vermögensschutzes. Wir helfen dabei, Vermögenswerte zu sichern. Für unseren Bereich Vermögensschutz benötigen wir eine Grafik, welche die Vorteile unseres Produkts direkt auf einen Blick erkennen lässt. Hierzu habe ich eine Grafik eines großen Mobilfunkherstellers beigefügt. Im gleichen Designe möchten wir diese Grafik haben.
Aufgabenstellung
Ich habe eine PDF-Datei (Vermögensschutz) beigefügt, aus welcher sich die Keyfacts ergeben. Diese müssen grafisch aufbereitet werden.

```html
<!DOCTYPE html>
<html lang="de">
<head>
<meta charset="utf-8">
<title>Vermögensschutz – Infografiken</title>
<link href="https://fonts.googleapis.com/css2?family=Arimo:wght@400;700&family=Hind:wght@400;500&display=swap" rel="stylesheet">
<style>
  :root{
    --bg:#e2dadb;
    --white:#ffffff;
    --ink:#1a1a1a;
    --crimson:#e2304f;
    --rose:#f0466a;
    --ruby:#cf1745;
    --purple:#7a0a6c;
    --magenta:#a5155a;
    --orange:#ff9a22;
    --amber:#ffbe00;
    --coral:#ff6a5a;
    --green:#6ab56f;
    --olive:#b3b83a;
    --teal:#1fb0b4;
    --icon:#6d6e78;
    --pct:#8c5ea6;
  }
  html,body{margin:0;padding:0;overflow:hidden;}
  body{width:1200px;height:800px;background:var(--bg);}
  .board{display:block;width:1200px;height:800px;}
  .t-light{font-family:"Hind",sans-serif;font-weight:400;fill:var(--ink);}
  .t-bold{font-family:"Arimo",sans-serif;font-weight:700;fill:var(--ink);}
  .t-regular{font-family:"Arimo",sans-serif;font-weight:400;fill:var(--ink);}
  .pill{fill:var(--white);filter:url(#soft-shadow);}
  .ring-shadow{filter:url(#soft-shadow);}
  .seg-label{font-family:"Arimo",sans-serif;font-weight:700;fill:var(--white);font-size:17px;letter-spacing:.5px;}
  .arrow-line{fill:none;stroke-width:9;stroke-linejoin:miter;}
  .icon-white{fill:none;stroke:var(--white);stroke-width:2.4;stroke-linecap:round;stroke-linejoin:round;}
</style>
</head>
<body>
<svg class="board" viewBox="0 0 1200 800" xmlns="http://www.w3.org/2000/svg">
  <defs>
    <filter id="soft-shadow" x="-20%" y="-20%" width="140%" height="150%">
      <feDropShadow dx="2" dy="4" stdDeviation="4" flood-color="#000" flood-opacity=".18"/>
    </filter>
    <linearGradient id="g-rose" x1="0" y1="0" x2="1" y2="1"><stop offset="0" stop-color="var(--rose)"/><stop offset="1" stop-color="var(--ruby)"/></linearGradient>
    <linearGradient id="g-sun" x1="0" y1="0" x2="1" y2="1"><stop offset="0" stop-color="var(--amber)"/><stop offset="1" stop-color="var(--coral)"/></linearGradient>
    <linearGradient id="g-leaf" x1="0" y1="0" x2="1" y2="1"><stop offset="0" stop-color="var(--amber)"/><stop offset=".55" stop-color="var(--green)"/><stop offset="1" stop-color="var(--teal)"/></linearGradient>
    <linearGradient id="g-orange-h" x1="0" y1="0" x2="1" y2="0"><stop offset="0" stop-color="var(--amber)"/><stop offset="1" stop-color="var(--coral)"/></linearGradient>
    <linearGradient id="g-coral-h" x1="0" y1="0" x2="1" y2="0"><stop offset="0" stop-color="var(--coral)"/><stop offset="1" stop-color="var(--orange)"/></linearGradient>
    <linearGradient id="g-green-h" x1="0" y1="0" x2="1" y2="0"><stop offset="0" stop-color="var(--amber)"/><stop offset="1" stop-color="var(--green)"/></linearGradient>
    <linearGradient id="g-teal-h" x1="0" y1="0" x2="1" y2="0"><stop offset="0" stop-color="var(--green)"/><stop offset="1" stop-color="var(--teal)"/></linearGradient>
    <linearGradient id="g-red-h" x1="0" y1="0" x2="1" y2="0"><stop offset="0" stop-color="var(--rose)"/><stop offset="1" stop-color="var(--ruby)"/></linearGradient>
    <linearGradient id="g-olive-h" x1="0" y1="0" x2="1" y2="0"><stop offset="0" stop-color="var(--green)"/><stop offset="1" stop-color="var(--amber)"/></linearGradient>
    <linearGradient id="g-sunset-h" x1="0" y1="0" x2="1" y2="0"><stop offset="0" stop-color="var(--orange)"/><stop offset="1" stop-color="var(--coral)"/></linearGradient>
  </defs>

  <!-- ===== Vorteile: Anonymität / Grunderwerbsteuer / Steueroptimierung ===== -->
  <g class="benefit-list">
    <g class="benefit">
      <circle cx="223" cy="137" r="49" fill="none" stroke="url(#g-rose)" stroke-width="10" stroke-dasharray="240 68" transform="rotate(-5 223 137)"/>
      <path class="pill" d="M250,93 H458 A44,44 0 0 1 458,180 H250 Z"/>
      <circle class="ring-shadow" cx="223" cy="137" r="31" fill="url(#g-rose)"/>
      <circle cx="258" cy="100" r="23" fill="url(#g-rose)"/>
      <circle cx="258" cy="100" r="15" fill="var(--white)"/>
      <circle cx="258" cy="100" r="6" fill="none" stroke="var(--crimson)" stroke-width="4" stroke-dasharray="2.2 1.6"/>
      <circle cx="258" cy="100" r="2" fill="var(--crimson)"/>
      <text class="t-light" x="223" y="144" font-size="15" text-anchor="middle" style="fill:var(--pct)">100%</text>
      <text class="t-light" x="309" y="116" font-size="16">Anonymität</text>
      <text class="t-light" x="298" y="142" font-size="16">Keine Rückschlüsse</text>
      <text class="t-light" x="298" y="161" font-size="16">auf Sie möglich</text>
    </g>
    <g class="benefit">
      <circle cx="223" cy="235" r="49" fill="none" stroke="url(#g-sun)" stroke-width="10" stroke-dasharray="240 68" transform="rotate(-5 223 235)"/>
      <path class="pill" d="M250,191 H458 A44,44 0 0 1 458,278 H250 Z"/>
      <circle class="ring-shadow" cx="223" cy="235" r="31" fill="url(#g-sun)"/>
      <circle cx="258" cy="198" r="23" fill="url(#g-sun)"/>
      <circle cx="258" cy="198" r="15" fill="var(--white)"/>
      <circle cx="258" cy="198" r="7" fill="none" stroke="var(--orange)" stroke-width="2"/>
      <path d="M258,194 V198 H261" fill="none" stroke="var(--orange)" stroke-width="1.5"/>
      <text class="t-light" x="223" y="245" font-size="26" text-anchor="middle">0%</text>
      <text class="t-light" x="295" y="227" font-size="16">Grunderwerbssteuer</text>
      <text class="t-light" x="295" y="247" font-size="16">freie Einbringung</text>
    </g>
    <g class="benefit">
      <circle cx="223" cy="332" r="49" fill="none" stroke="url(#g-leaf)" stroke-width="10" stroke-dasharray="240 68" transform="rotate(-5 223 332)"/>
      <path class="pill" d="M250,289 H458 A44,44 0 0 1 458,376 H250 Z"/>
      <circle class="ring-shadow" cx="223" cy="332" r="31" fill="url(#g-leaf)"/>
      <circle cx="258" cy="296" r="23" fill="url(#g-leaf)"/>
      <circle cx="258" cy="296" r="15" fill="var(--white)"/>
      <circle cx="258" cy="293" r="6" fill="var(--green)"/>
      <rect x="255" y="299" width="6" height="4" fill="var(--green)"/>
      <path d="M255.5,293 l2,2 l3.5,-4" fill="none" stroke="var(--white)" stroke-width="1.4"/>
      <text class="t-light" x="295" y="318" font-size="16">Steueroptimierung</text>
      <text class="t-light" x="295" y="337" font-size="16">für das laufende</text>
      <text class="t-light" x="295" y="357" font-size="16">Einkommen</text>
    </g>
  </g>

  <!-- ===== Sicherung von Vermögenswerten ===== -->
  <g class="asset-wheel">
    <g class="ring-shadow" fill="none" stroke-width="52">
      <circle cx="825" cy="221" r="118" stroke="var(--crimson)" stroke-dasharray="92.7 648.7" transform="rotate(-90 825 221)"/>
      <circle cx="825" cy="221" r="118" stroke="var(--orange)" stroke-dasharray="92.7 648.7" transform="rotate(-45 825 221)"/>
      <circle cx="825" cy="221" r="118" stroke="var(--coral)" stroke-dasharray="92.7 648.7" transform="rotate(0 825 221)"/>
      <circle cx="825" cy="221" r="118" stroke="var(--teal)" stroke-dasharray="92.7 648.7" transform="rotate(45 825 221)"/>
      <circle cx="825" cy="221" r="118" stroke="var(--green)" stroke-dasharray="92.7 648.7" transform="rotate(90 825 221)"/>
      <circle cx="825" cy="221" r="118" stroke="var(--magenta)" stroke-dasharray="92.7 648.7" transform="rotate(135 825 221)"/>
      <circle cx="825" cy="221" r="118" stroke="var(--purple)" stroke-dasharray="92.7 648.7" transform="rotate(180 825 221)"/>
      <circle cx="825" cy="221" r="118" stroke="var(--rose)" stroke-dasharray="92.7 648.7" transform="rotate(225 825 221)"/>
    </g>
    <circle cx="825" cy="221" r="74" fill="var(--white)" filter="url(#soft-shadow)"/>

    <text class="seg-label" transform="translate(779 113) rotate(-22)" text-anchor="middle">Auto</text>
    <text class="seg-label" transform="translate(927 172) rotate(70)" text-anchor="middle">Flugz</text>
    <text class="seg-label" transform="translate(866 338) rotate(-20)" text-anchor="middle">Uhren</text>
    <text class="seg-label" transform="translate(708 251) rotate(80)" text-anchor="middle">Boot</text>

    <g class="icon-gear">
      <circle cx="867" cy="123" r="8" fill="none" stroke="var(--white)" stroke-width="5" stroke-dasharray="3 2"/>
      <circle cx="867" cy="123" r="6" fill="var(--white)"/>
      <circle cx="867" cy="123" r="2.5" fill="var(--crimson)"/>
    </g>
    <g class="icon-bulb">
      <circle cx="916" cy="261" r="9" fill="var(--white)"/>
      <rect x="912" y="270" width="8" height="5" rx="1" fill="var(--white)"/>
      <path d="M912,261 l3,3 l5,-6" fill="none" stroke="var(--coral)" stroke-width="2"/>
    </g>
    <g class="icon-clock">
      <circle class="icon-white" cx="780" cy="320" r="9"/>
      <path class="icon-white" d="M780,315 V320 H783"/>
    </g>
    <g class="icon-chat">
      <path d="M727,171 a10,9 0 1 1 5,8 l-6,3 z" fill="var(--white)"/>
      <circle cx="722" cy="178" r="1.3" fill="var(--purple)"/>
      <circle cx="727" cy="178" r="1.3" fill="var(--purple)"/>
      <circle cx="732" cy="178" r="1.3" fill="var(--purple)"/>
    </g>
    <g class="icon-chart" fill="var(--icon)">
      <rect x="812" y="184" width="5" height="10"/>
      <rect x="820" y="180" width="5" height="14"/>
      <rect x="828" y="176" width="5" height="18"/>
      <path d="M810,176 l9,-5 l8,6 l12,-11" fill="none" stroke="var(--icon)" stroke-width="2.4"/>
      <path d="M834,164 h7 v7 z"/>
    </g>
    <text class="t-light" x="825" y="219" font-size="18" text-anchor="middle">Sicherung von</text>
    <text class="t-light" x="820" y="242" font-size="18" text-anchor="middle">Vermögenswerten</text>

    <text class="t-light" x="692" y="110" font-size="12" text-anchor="middle">Immobilien</text>
    <text class="t-light" x="961" y="110" font-size="12" text-anchor="middle">Barvermögen</text>
    <text class="t-light" x="667" y="324" font-size="12" text-anchor="middle">Kryptowährung</text>
    <text class="t-light" x="977" y="324" font-size="12" text-anchor="middle">Firmenanteile</text>
  </g>

  <!-- ===== Schutz vor Ansprüchen Dritter ===== -->
  <g class="claims">
    <g class="arrows">
      <path class="arrow-line" stroke="url(#g-red-h)" d="M270,490 L293,466 H414 L428,440 L406,410"/>
      <path class="arrow-line" stroke="var(--ruby)" d="M314,532 H449 L462,505 L442,477"/>
      <path class="arrow-line" stroke="url(#g-olive-h)" d="M330,593 H474 L489,567 L472,540"/>
      <path class="arrow-line" stroke="url(#g-olive-h)" d="M300,660 H455 L469,633 L452,606"/>
      <path class="arrow-line" stroke="url(#g-sunset-h)" d="M255,688 L290,724 H456 L478,700 L447,672"/>
    </g>
    <g class="ring-shadow" fill="none" stroke-width="33">
      <circle cx="228" cy="585" r="88" stroke="var(--crimson)" stroke-dasharray="138.2 414.7" transform="rotate(-135 228 585)"/>
      <circle cx="228" cy="585" r="88" stroke="var(--purple)" stroke-dasharray="69.1 483.8" transform="rotate(-45 228 585)"/>
      <circle cx="228" cy="585" r="88" stroke="var(--teal)" stroke-dasharray="69.1 483.8" transform="rotate(0 228 585)" opacity=".85"/>
      <circle cx="228" cy="585" r="88" stroke="var(--orange)" stroke-dasharray="138.2 414.7" transform="rotate(45 228 585)"/>
      <circle cx="228" cy="585" r="88" stroke="var(--green)" stroke-dasharray="69.1 483.8" transform="rotate(135 228 585)"/>
      <circle cx="228" cy="585" r="88" stroke="var(--purple)" stroke-dasharray="69.1 483.8" transform="rotate(180 228 585)"/>
    </g>
    <circle cx="228" cy="585" r="72" fill="var(--white)" filter="url(#soft-shadow)"/>
    <g class="icon-bulb">
      <circle cx="225" cy="543" r="9" fill="var(--icon)"/>
      <rect x="221" y="552" width="8" height="5" rx="1" fill="var(--icon)"/>
      <path d="M221,543 l3,3 l5,-6" fill="none" stroke="var(--white)" stroke-width="2"/>
    </g>
    <text class="t-bold" x="232" y="576" font-size="17" text-anchor="middle">Schutz vor</text>
    <text class="t-bold" x="229" y="596" font-size="17" text-anchor="middle">Ansprüchen</text>
    <text class="t-bold" x="229" y="617" font-size="17" text-anchor="middle">Dritter</text>

    <text class="t-bold" x="337" y="446" font-size="17" text-anchor="middle">Bank</text>
    <text class="t-bold" x="376" y="510" font-size="17" text-anchor="middle">Finanzamt</text>
    <text class="t-bold" x="407" y="574" font-size="17" text-anchor="middle">Bürgschaften</text>
    <text class="t-bold" x="374" y="639" font-size="17" text-anchor="middle">Klage</text>
    <text class="t-bold" x="368" y="704" font-size="17" text-anchor="middle">Sozialversicherung</text>
  </g>

  <!-- ===== Steuer- und Insolvenzvorteile ===== -->
  <g class="banners">
    <g class="banner">
      <path d="M737,410 H965 A40,40 0 0 1 965,490 H790 C768,470 758,432 737,410 Z" fill="url(#g-orange-h)"/>
      <path d="M708,408 A51,51 0 0 0 708,510 H797 C770,485 760,430 737,410 Z" fill="url(#g-coral-h)"/>
      <circle cx="708" cy="459" r="36" fill="var(--white)" filter="url(#soft-shadow)"/>
      <text class="t-bold" x="708" y="471" font-size="32" text-anchor="middle">0%</text>
      <text class="t-regular" x="874" y="443" font-size="17" text-anchor="middle">Wegzugsbesteuerung</text>
      <text class="t-regular" x="883" y="466" font-size="17" text-anchor="middle">Freiheit</text>
    </g>
    <g class="banner">
      <path d="M926,520 H698 A40,40 0 0 0 698,600 H892 C910,580 912,540 926,520 Z" fill="url(#g-green-h)"/>
      <path d="M959,519 A51,51 0 0 1 959,621 H867 C893,598 903,545 926,520 Z" fill="url(#g-teal-h)"/>
      <circle cx="959" cy="570" r="36" fill="var(--white)" filter="url(#soft-shadow)"/>
      <text class="t-bold" x="959" y="582" font-size="32" text-anchor="middle">0%</text>
      <text class="t-regular" x="772" y="563" font-size="17" text-anchor="middle">Erbschaftssteuer</text>
    </g>
    <g class="banner">
      <path d="M737,629 H965 A40,40 0 0 1 965,709 H790 C768,689 758,651 737,629 Z" fill="url(#g-red-h)"/>
      <path d="M708,628 A51,51 0 0 0 708,730 H797 C770,705 760,650 737,629 Z" fill="var(--rose)"/>
      <circle cx="708" cy="679" r="36" fill="var(--white)" filter="url(#soft-shadow)"/>
      <text class="t-bold" x="708" y="689" font-size="25" text-anchor="middle">100%</text>
      <text class="t-regular" x="814" y="652" font-size="16">Insolvenz sicher</text>
      <text class="t-regular" x="814" y="673" font-size="16">Kein Zugriff vom</text>
      <text class="t-regular" x="814" y="693" font-size="16">Insolvenzverwalter</text>
    </g>
  </g>
</svg>
</body>
</html>
```